Business Broker Website

Hi.
I need a new design done for a business broker website. An example of the style of website I like is https://marlowvantage.example/
The menu needs to be :
* Home
* Businesses for Sale
* What we do
* Our people
* Industries
* Blog
* Confidentiality
* Contact
The home page needs to include a section saying 'businesses sold' with each having a photo, heading and short description. It also needs to have a place to show a video which I have attached so you can take a screenshot to put it on the page.
The content on the home page needs to be as follows:
Harbourline Ventures Group are a boutique brokerage business, specializing in the sales and marketing of SME businesses throughout Queensland and, the Northern Territory
who we are
Welcome to Harbourline Ventures Group. Our specialization is in the marketing and acquisition of closely held businesses throughout Queensland and the Northern Territory. We concentrate in SME businesses in the turnovers of approximately $1,000,000 to $10,000,000 +.
The combined business experience and industry knowledge of our principal is unparalleled and fully committed to a “customer first always” approach to doing business.
Our seller’s benefit from a multi-faceted strategic marketing plan, custom prepared for each seller, no two marketing campaigns are the same. This assures maximum exposure to well-qualified Buyers, while strictly maintaining confidentiality.
We have the comprehensive knowledge and resources to help our Buyers identify their perfect business acquisition– perhaps even if that business is not currently listed for sale!
"the whole secret of a successful life is to find out what is one's destiny to do, and then do it." walter pryce
people looking to buy or sell businesses
1 page

```html
<!DOCTYPE html>
<html lang="en">
<head>
<meta charset="utf-8">
<title>Harbourline Ventures Group</title>
<link href="https://fonts.googleapis.com/css2?family=Montserrat:wght@400;500;600;700&family=Oswald:wght@400&family=Arimo:wght@400;700&display=swap" rel="stylesheet">
<style>
:root{
  --purple:#5a3d8c;
  --purple-dark:#4a2f78;
  --ink:#2a2a2a;
  --body:#555;
  --black:#0d0d0d;
  --line:#d8d8d8;
  --white:#fff;
}
*{box-sizing:border-box;margin:0;padding:0}
html,body{width:1200px;height:4110px;overflow:hidden;background:var(--white)}
body{position:relative;font-family:"Montserrat",sans-serif;color:var(--body)}
.abs{position:absolute}
.btn{position:absolute;display:flex;align-items:center;justify-content:center;border-radius:22px;background:var(--purple);color:var(--white);font:600 13px "Montserrat",sans-serif}
.btn.light{background:var(--white);color:var(--ink)}

/* header */
.site-header{left:0;top:0;width:1200px;height:70px;background:var(--white)}
.brand{position:absolute;display:flex;align-items:center;gap:10px}
.brand-dot{width:44px;height:44px;border-radius:50%;background:var(--purple)}
.brand-name{font:700 19px/1.05 "Montserrat",sans-serif;color:var(--purple)}
.main-nav{position:absolute;left:428px;top:26px;display:flex;gap:17.5px;font:500 12px "Montserrat",sans-serif;color:var(--ink)}
.main-nav .active{color:var(--purple)}

/* hero */
.hero{left:0;top:70px;width:1200px;height:495px;background:linear-gradient(180deg,#c9ccd2 0%,#8d8f96 40%,#3a3a3e 75%,#0f0f12 100%)}
.hero h1{position:absolute;left:0;top:330px;width:1200px;text-align:center;font:400 38px/42px "Oswald",sans-serif;color:var(--white)}
.enquiry{left:140px;top:519px;width:918px;height:164px;background:var(--white);box-shadow:0 4px 18px rgba(0,0,0,.12)}
.enquiry h2{position:absolute;top:26px;width:100%;text-align:center;font:600 31px "Montserrat",sans-serif;color:var(--purple)}
.enquiry .rule{position:absolute;left:439px;top:70px;width:42px;height:2px;background:var(--purple)}
.field{position:absolute;top:92px;height:42px;border:1px solid var(--line);font:500 12px/40px "Montserrat",sans-serif;color:var(--ink);padding-left:13px}
.enquiry .send{position:absolute;left:804px;top:92px;width:98px;height:41px;background:var(--purple);color:var(--white);font:500 17px/41px "Montserrat",sans-serif;text-align:center}

/* businesses for sale */
.video-frame{left:140px;top:785px;width:364px;height:364px;border-radius:50%;border:2px solid #444;background:radial-gradient(circle at 50% 40%,#d9d9d9,#b9c3cf 60%,#a9b2bd)}
.play{left:420px;top:1045px;width:96px;height:96px;border-radius:50%;background:var(--white);box-shadow:0 3px 12px rgba(0,0,0,.2)}
.sale-copy{left:616px;top:800px;width:440px}
.sale-copy h2{font:700 36px "Arimo",sans-serif;color:var(--purple);margin-bottom:10px}
.copy{font:400 12.4px/23px "Montserrat",sans-serif;color:var(--body);letter-spacing:.15px}
.copy p+p{margin-top:9px}

/* dark band */
.band{left:0;top:1219px;width:1200px;height:381px;background:radial-gradient(ellipse at 55% 60%,#6a4632 0%,#2e2622 40%,#141414 80%)}
.band p{position:absolute;top:95px;width:100%;text-align:center;font:600 25.5px/41px "Montserrat",sans-serif;color:var(--white);letter-spacing:.5px}

/* who we are */
.who-title{left:0;top:1668px;width:1200px;text-align:center;font:700 35px "Arimo",sans-serif;color:var(--purple)}
.who-intro{left:180px;top:1721px;width:840px;text-align:center}
.who-body{left:142px;top:1821px;width:460px;text-align:justify;letter-spacing:.6px}
.who-body b{color:var(--purple);font-weight:700}
.who-photo{left:695px;top:1811px;width:363px;height:367px;border-radius:50%;background:radial-gradient(circle at 60% 35%,#8a6a5c,#3d3550 55%,#243a2e)}

/* services */
.svc-photo{left:19px;top:2253px;width:546px;height:479px;background:linear-gradient(135deg,#e9ecef 0%,#b8c0c8 45%,#26324a 70%,#dfe3e6 100%)}
.svc{top:2253px;width:318px;height:479px;color:var(--white)}
.svc.sales{left:565px;background:var(--purple)}
.svc.mkt{left:882px;background:var(--black)}
.svc svg{position:absolute;left:29px;top:76px}
.svc h3{position:absolute;left:29px;top:166px;font:700 23px "Arimo",sans-serif}
.svc p{position:absolute;left:29px;top:209px;width:262px;font:400 11.6px/22.5px "Montserrat",sans-serif;color:#e6e0ef}
.svc .plus{position:absolute;left:29px;top:361px;width:43px;height:41px;border:1px solid var(--white);font:400 20px/39px "Montserrat",sans-serif;text-align:center}

/* blog */
.blog-title{left:0;top:2798px;width:1200px;text-align:center;font:700 35px "Arimo",sans-serif;color:var(--purple)}
.card{border:1px solid #e3e3e3;border-radius:6px;overflow:hidden;background:var(--white)}
.card .img{position:absolute}
.card h4{position:absolute;font:700 17.5px/27px "Arimo",sans-serif;color:var(--ink)}
.card .date{position:absolute;font:400 12.5px "Montserrat",sans-serif;color:var(--purple)}
.card .excerpt{position:absolute;font:400 12.4px/22px "Montserrat",sans-serif;color:var(--body)}
.card .more{position:absolute;font:600 13px "Montserrat",sans-serif;color:var(--purple);text-decoration:underline}

/* cta */
.cta{left:0;top:3511px;width:1200px;height:183px;background:linear-gradient(180deg,#5b3f8c,#4a2f78)}
.cta p{position:absolute;left:147px;top:55px;font:600 28px/39px "Arimo",sans-serif;color:var(--white)}

/* footer */
.foot-h{font:700 18.5px "Arimo",sans-serif;color:var(--purple)}
.quick{list-style:none;font:400 13px/25.5px "Montserrat",sans-serif;color:var(--body)}
.quick li::before{content:"›";margin-right:10px}
.contact-item{position:absolute;left:420px;font:400 13px/23px "Montserrat",sans-serif;color:var(--body)}
.contact-item .lbl{font-size:15px}
.ico{position:absolute;left:365px}
.social{position:absolute;top:3900px;width:30px;height:30px;border-radius:50%;border:1.5px solid #555}
.foot-rule{left:142px;top:4063px;width:916px;height:1px;background:var(--line)}
.copyright{left:0;top:4079px;width:1200px;text-align:center;font:400 12.5px "Montserrat",sans-serif;color:var(--body)}
</style>
</head>
<body>

<header class="site-header abs">
  <div class="brand" style="left:147px;top:12px">
    <span class="brand-dot"></span>
    <span class="brand-name">Harbourline Ventures<br>Group</span>
  </div>
  <nav class="main-nav">
    <span class="active">Home</span><span>Businesses For Sale</span><span>What We Do</span><span>Our People</span><span>Industries</span><span>Blog</span><span>Confidentiality</span><span>Contact</span>
  </nav>
</header>

<section class="hero abs" role="img" aria-label="Photo of business people shaking hands in an office">
  <h1>Harbourline Ventures Group Is A Marketing Consulting Firm That<br>Introduces Businesses To New Opportunities For Growth</h1>
</section>

<form class="enquiry abs">
  <h2>We Will Find You The Perfect Company To Buy</h2>
  <span class="rule"></span>
  <div class="field" style="left:26px;width:160px">Name</div>
  <div class="field" style="left:202px;width:160px">Phone</div>
  <div class="field" style="left:378px;width:160px">Email</div>
  <div class="field" style="left:554px;width:234px">Message</div>
  <div class="send">Send</div>
</form>

<div class="video-frame abs" role="img" aria-label="Video still: illustrated industry overview with a presenter"></div>
<div class="play abs">
  <svg width="96" height="96" viewBox="0 0 96 96"><circle cx="48" cy="48" r="31" fill="none" stroke="#bbb" stroke-width="3"/><path d="M40 34 L62 48 L40 62Z" fill="#bbb"/></svg>
</div>
<div class="sale-copy abs">
  <h2>businesses for sale</h2>
  <div class="copy">
    <p>Mauris dui mauris, lacinia vel lacus et, faucibus egestas nibh. Sedt lobortis lorem magna, id fringilla magna faucibus in. Donec dernrt aliquam, turpis ac commodo vehicula, tellus mauris porta ante, id hendrerit augue nisl eu velit.</p>
    <p>In non eleifend eros, a dapibus massa. Vestibulum sollicitudin ante sit amet ligula luctus, vitae pretium nibh euismod. Suspendisse sit amet nulla libero. Quisque sodales scelerisque turpisen eu laoreet lectus imperdiet sit amet etiam ante nisl, tempus eget tortorrt tet vehicula tincidunt lacus.</p>
  </div>
</div>
<div class="btn" style="left:616px;top:1080px;width:140px;height:43px">read more</div>

<section class="band abs" role="img" aria-label="Photo of a handshake with business silhouettes">
  <p>Harbourline Ventures Group are a boutique brokerage business,<br>specializing in the sales and marketing of SME businesses<br>throughout Queensland &amp;, the Northern Territory</p>
</section>
<div class="btn light" style="left:515px;top:1455px;width:170px;height:42px">contact us today</div>

<h2 class="who-title abs">who we are</h2>
<p class="who-intro abs copy">Welcome to Harbourline Ventures Group. Our specialization is in the marketing and acquisition of closely held businesses throughout Queensland and the Northern Territory. We concentrate in SME businesses in the turnovers of approximately $1,000,000 to $10,000,000 +</p>
<div class="who-body abs copy">
  <p>The combined business experience and industry knowledge of our principal is unparalleled and fully committed to a “customer first always” approach to doing business. Our seller’s benefit from a multi-faceted strategic marketing plan, custom prepared for each seller, no two marketing campaigns are the same. This assures maximum exposure to well-qualified Buyers, while strictly maintaining confidentiality.</p>
  <p>We have the comprehensive knowledge and resources to help our Buyers identify their perfect business acquisition– perhaps even if that business is not currently listed for sale!“the whole secret of a successful life is to find out what is one's destiny to do, and then do it.” <b>Walter Pryce</b></p>
</div>
<div class="btn" style="left:142px;top:2127px;width:168px;height:42px">contact us today</div>
<div class="who-photo abs" role="img" aria-label="Photo of a smiling businessman at a conference, framed in a swooping circle"></div>

<div class="svc-photo abs" role="img" aria-label="Photo of two businessmen reviewing charts on a laptop"></div>
<section class="svc sales abs">
  <svg width="82" height="70" viewBox="0 0 82 70" fill="none" stroke="#fff" stroke-width="2"><rect x="4" y="44" width="10" height="22"/><rect x="19" y="36" width="10" height="30"/><rect x="34" y="28" width="10" height="38"/><rect x="49" y="18" width="10" height="48"/><rect x="64" y="8" width="10" height="58"/><path d="M2 36 L36 14 L60 4" /><path d="M0 68 H80"/></svg>
  <h3>sales</h3>
  <p>Orci varius natoque penatibus et magnis dis parturient montes, nascetur ridiculus mus. Integer at mauris orci. Fusce tempor pellentesque ex. Morbi nisl augue, suscipit et feugiat sed vitae egestas nunc tellus at elit morbi imperdiet tellus eget.</p>
  <div class="plus">+</div>
</section>
<section class="svc mkt abs">
  <svg width="76" height="72" viewBox="0 0 76 72" fill="none" stroke="#fff" stroke-width="2"><path d="M4 30 H16 L40 18 V58 L16 46 H4Z"/><path d="M10 46 L16 64 H24 L20 46"/><circle cx="36" cy="6" r="4"/><circle cx="28" cy="12" r="3"/><path d="M58 10 a5 5 0 0 1 8 0 a5 5 0 0 1 8 0 L66 20Z"/><circle cx="60" cy="46" r="6"/><rect x="48" y="28" width="14" height="12"/></svg>
  <h3>marketing</h3>
  <p>Orci varius natoque penatibus et magnis dis parturient montes, nascetur ridiculus mus. Integer at mauris orci. Fusce tempor pellentesque ex. Morbi nisl augue, suscipit et feugiat sed vitae egestas nunc tellus at elit morbi imperdiet tellus eget.</p>
  <div class="plus">+</div>
</section>

<h2 class="blog-title abs">latest Blog posts</h2>
<article class="card abs" style="left:142px;top:2882px;width:414px;height:478px">
  <div class="img" style="left:0;top:0;width:414px;height:233px;background:linear-gradient(180deg,#e8e6e2,#9a8f86 60%,#5d5a58)" role="img" aria-label="Photo of a team meeting around a conference table"></div>
  <h4 style="left:20px;top:253px;width:370px">Mauris dui mauris lacinia vel lacus faucit egestas nibh sed lobortis</h4>
  <div class="date" style="left:20px;top:318px">January 25, 2022</div>
  <p class="excerpt" style="left:20px;top:345px;width:380px">Orci varius natoque penatibus et magnis dparturient montes, nascetur ridiculus mus integer at mauris orc fusce tempor pellentesqu exmorb nisl augue.</p>
  <span class="more" style="left:20px;top:431px">Learn More</span>
</article>
<article class="card abs" style="left:582px;top:2882px;width:476px;height:234px">
  <div class="img" style="left:0;top:0;width:213px;height:234px;background:linear-gradient(135deg,#dfe8f3,#93aed2 60%,#6f8fbf)" role="img" aria-label="Photo of a handshake over a digital network"></div>
  <h4 style="left:232px;top:18px;width:230px">Orci varius natoque penet et magnis dis partur</h4>
  <div class="date" style="left:232px;top:82px">January 25, 2022</div>
  <p class="excerpt" style="left:232px;top:108px;width:225px">Etiam ante nisl, tempus egetrt tortor et, vehicula tincidunt at lacus cras sed massa.</p>
  <span class="more" style="left:232px;top:189px">Learn More</span>
</article>
<article class="card abs" style="left:582px;top:3126px;width:476px;height:234px">
  <div class="img" style="left:0;top:0;width:213px;height:234px;background:linear-gradient(180deg,#1b2a5a,#3b4f8a 55%,#1a2246)" role="img" aria-label="Photo of business silhouettes against a city window"></div>
  <h4 style="left:232px;top:18px;width:230px">Orci varius natoque penet et magnis dis partur</h4>
  <div class="date" style="left:232px;top:82px">January 25, 2022</div>
  <p class="excerpt" style="left:232px;top:108px;width:225px">Etiam ante nisl, tempus egetrt tortor et, vehicula tincidunt at lacus cras sed massa.</p>
  <span class="more" style="left:232px;top:189px">Learn More</span>
</article>
<div class="btn" style="left:530px;top:3396px;width:140px;height:43px">view all blogs</div>

<section class="cta abs">
  <p>as a company, we design and implement a new<br>customer-centric approach to achieve client growth</p>
</section>
<div class="btn light" style="left:882px;top:3581px;width:170px;height:43px">contact us today</div>

<footer>
  <h5 class="foot-h abs" style="left:142px;top:3764px">Quick links</h5>
  <ul class="quick abs" style="left:142px;top:3797px">
    <li>Home</li><li>Businesses For Sale</li><li>What We Do</li><li>Our People</li><li>Industries</li><li>Blog</li><li>Confidentiality</li><li>Contact</li>
  </ul>
  <h5 class="foot-h abs" style="left:369px;top:3764px">Contact details</h5>
  <svg class="ico" style="top:3810px" width="30" height="30" viewBox="0 0 30 30" fill="none" stroke="#555" stroke-width="1.4"><path d="M15 3 a8 8 0 0 1 8 8 c0 6 -8 15 -8 15 s-8 -9 -8 -15 a8 8 0 0 1 8 -8Z"/><circle cx="15" cy="11" r="3"/></svg>
  <div class="contact-item" style="top:3799px">14 Wharf Lane, Riverside<br>Port Ellis, Queensland 4870</div>
  <svg class="ico" style="top:3876px" width="30" height="30" viewBox="0 0 30 30" fill="none" stroke="#555" stroke-width="1.4"><path d="M8 4 L12 4 L14 10 L11 12 C12 16 14 18 18 19 L20 16 L26 18 L26 22 C26 24 24 26 22 26 C12 25 5 18 4 8 C4 6 6 4 8 4Z"/></svg>
  <div class="contact-item" style="top:3867px"><span class="lbl">Phone</span><br>+61 (0) 7 5550 1842</div>
  <svg class="ico" style="top:3946px" width="30" height="30" viewBox="0 0 30 30" fill="none" stroke="#555" stroke-width="1.4"><rect x="3" y="8" width="24" height="18"/><path d="M3 8 L15 18 L27 8"/></svg>
  <div class="contact-item" style="top:3936px"><span class="lbl">Email</span><br>inquiry@harbourlineventures.example</div>
  <div class="brand" style="left:771px;top:3818px">
    <span class="brand-dot" style="width:52px;height:52px"></span>
    <span class="brand-name" style="font-size:22px">Harbourline Ventures<br>Group</span>
  </div>
  <span class="social" style="left:853px"></span>
  <span class="social" style="left:893px"></span>
  <span class="social" style="left:933px"></span>
  <div class="foot-rule abs"></div>
  <p class="copyright abs">Copyright © 2022 harbourline ventures group. All Rights Reserved.</p>
</footer>

</body>
</html>
```